2018 Season - Production Graphics

We need custom graphics for each production in our 2018 season. The shows in the 2018 season are attached with descriptions of each show. The graphics should be family-friendly, but completely different than the original graphic. We'd like to portray a "Halvenmoor in a small town" feel. Our audience is usually familiar with the plays we put on, so designing something completely different than the traditional graphics is encouraged.

Target Market(s)

Families, Arts Enthusiasts

Industry/Entity Type

Entertainment

Font styles to use
Sans Serif

Colors

Designer to choose colors to be used in the design.

Requirements
Must have
• A graphic for each production that includes name of production and imagery that ties into the plot.

```html
<!DOCTYPE html>
<html lang="en">
<head>
<meta charset="UTF-8">
<title>The Crucible – February 16th–18th</title>
<link rel="stylesheet" href="https://fonts.googleapis.com/css2?family=Oswald:wght@400&family=Roboto+Condensed:wght@400;700&display=swap">
<style>
  :root {
    --ink: #ffffff;
    --night: #050302;
    --shadow: #140a03;
    --ember: #e09a4a;
    --glow: #f3bd72;
    --dusk: #8a4f18;
    --plank: #6e3a12;
  }
  html, body {
    margin: 0;
    padding: 0;
    width: 1200px;
    height: 848px;
    overflow: hidden;
    background: var(--night);
  }
  .poster {
    position: relative;
    width: 1200px;
    height: 848px;
    overflow: hidden;
    background: var(--night);
    color: var(--ink);
  }
  .sky-glow {
    position: absolute;
    inset: 0;
    background:
      radial-gradient(ellipse 48% 40% at 66% 50%, var(--glow) 0%, var(--ember) 45%, var(--dusk) 80%, transparent 100%),
      linear-gradient(to right, var(--night) 0%, var(--shadow) 14%, transparent 26%),
      linear-gradient(to bottom, var(--night) 0%, var(--shadow) 20%, #3a1e07 45%, var(--shadow) 78%, var(--night) 100%);
  }
  .stage-set {
    position: absolute;
    inset: 0;
  }
  .dancers {
    position: absolute;
    left: 140px;
    top: 290px;
    width: 880px;
    height: 380px;
    background: radial-gradient(ellipse 60% 70% at 50% 65%, rgba(5,3,2,0.92) 0%, rgba(5,3,2,0.75) 55%, rgba(5,3,2,0) 100%);
  }
  .title,
  .run-dates {
    position: absolute;
    left: 50%;
    margin: 0;
    white-space: nowrap;
    font-family: "Oswald", sans-serif;
    font-weight: 400;
    line-height: 1;
    transform: translateX(-50%) scaleX(0.64);
  }
  .title {
    top: 44px;
    font-size: 198px;
    letter-spacing: -2px;
  }
  .run-dates {
    top: 630px;
    font-size: 94px;
    letter-spacing: -1px;
  }
  .director {
    position: absolute;
    top: 738px;
    left: 0;
    width: 100%;
    margin: 0;
    text-align: center;
    font-family: "Roboto Condensed", sans-serif;
    font-weight: 400;
    font-size: 38px;
    line-height: 1;
  }
  .director strong {
    font-weight: 700;
    letter-spacing: 0.5px;
  }
</style>
</head>
<body>
  <main class="poster">
    <div class="sky-glow"></div>
    <svg class="stage-set" width="1200" height="848" viewBox="0 0 1200 848" aria-hidden="true">
      <rect class="gallows-beam" x="480" y="228" width="376" height="34" fill="#070403"/>
      <rect class="gallows-post" x="612" y="250" width="52" height="420" fill="#070403"/>
      <rect class="stage-floor" x="0" y="640" width="1200" height="208" fill="#0a0502"/>
      <g class="floor-planks" stroke="var(--plank)" stroke-width="3" opacity="0.7">
        <line x1="0" y1="690" x2="200" y2="660"/>
        <line x1="0" y1="715" x2="210" y2="682"/>
        <line x1="0" y1="740" x2="190" y2="706"/>
        <line x1="990" y1="660" x2="1200" y2="690"/>
        <line x1="980" y1="684" x2="1200" y2="716"/>
        <line x1="990" y1="708" x2="1200" y2="742"/>
      </g>
    </svg>
    <div class="dancers" role="img" aria-label="Silhouettes of six young women in long dresses dancing in the woods with raised arms beneath a gnarled tree"></div>
    <h1 class="title">The Crucible</h1>
    <p class="run-dates">February 16th - 18th</p>
    <p class="director">Directed by: <strong>TOM HARTWELL</strong></p>
  </main>
</body>
</html>
```